Banner Ad Design Project for Muslim Fashion Site

I need banner ads for an e-commerce site selling modern muslim fashion, called "Selvarina.com". It is a flash sale site selling top designer brands of muslim fashion. The key driver of purchase is accessing special sale events for members, which goes up to 90% discount on certain brands.

We would like our logo "selvarina.com" to be part of the visual. You can get this logo on the top right of our site landing page (selvarina.com). The main visual should show an attractive lady with a modern looking hijab, if possible, with eye contact to the user, but not mandatory.

I am looking at very minimum 5 types of banner ad sizes:
728 x 90
120 x 600
300x 250
234 x 60
125 x125

3 concept variations are required.

Target Market(s)

asian modern muslim woman

Industry/Entity Type

E-Commerce

Requirements
Must have
• selvarina.com logo
attractive woman wearing modern looking hijab
the number "90%" to represent the discount on offer
the word "click here" as a call to action

```html
<!DOCTYPE html>
<html lang="en">
<head>
<meta charset="utf-8">
<title>Selvarina.com – Sale Banner</title>
<link rel="stylesheet" href="https://fonts.googleapis.com/css2?family=Arimo:wght@400&family=Tinos&display=swap">
<style>
  :root {
    --bg: #000000;
    --headline: #9fb39a;
    --headline-glow: #3e5a3c;
    --button: #3f7f74;
    --button-edge: #2c5f56;
    --button-text: #0e1e1b;
    --photo-top: #3a3a3a;
    --photo-bottom: #1a1a1a;
  }
  html, body {
    margin: 0;
    padding: 0;
    width: 1200px;
    height: 240px;
    overflow: hidden;
    background: var(--bg);
  }
  .banner {
    position: relative;
    width: 1200px;
    height: 240px;
    background: var(--bg);
    font-family: "Arimo", Arial, sans-serif;
  }
  .model-photo {
    position: absolute;
    left: 0;
    top: 0;
    width: 150px;
    height: 240px;
    background: linear-gradient(180deg, var(--photo-top), var(--photo-bottom));
  }
  .brand-name {
    position: absolute;
    left: 184px;
    top: 124px;
    margin: 0;
    font-size: 30px;
    font-weight: 400;
    color: var(--headline);
    white-space: nowrap;
  }
  .headline {
    position: absolute;
    left: 414px;
    top: 12px;
    margin: 0;
    font-size: 44px;
    font-weight: 400;
    letter-spacing: 1.3px;
    color: var(--headline);
    text-shadow: 0 0 4px var(--headline-glow), 0 0 8px var(--headline-glow);
    white-space: nowrap;
  }
  .cta {
    position: absolute;
    left: 844px;
    top: 148px;
    width: 178px;
    height: 76px;
    border-radius: 16px;
    background: var(--button);
    box-shadow: inset 0 -3px 0 var(--button-edge);
    display: flex;
    align-items: center;
    justify-content: center;
    font-family: "Tinos", "Times New Roman", serif;
    font-size: 24px;
    color: var(--button-text);
    text-decoration: none;
  }
</style>
</head>
<body>
  <div class="banner">
    <div class="model-photo" role="img" aria-label="Woman wearing a dark modern hijab, looking at the viewer"></div>
    <p class="brand-name">selvarina.com</p>
    <h1 class="headline">up to 90% discount on certain brands</h1>
    <a class="cta" href="#">CLICK HERE</a>
  </div>
</body>
</html>
```